Redesign of existing business card

I would like the "signage" attachment converted into a business card. This needs to be double sided aswell, keeping the phone number and names on the front, and the email + website on the back.

Second attachment is the current business card design.

Larger font for contact details is required.

Must keep to original color themes (electric blue, silver/grey etc)

Back of the card to have blue background with white writing.

Industry/Entity Type

Business

Contact Information for Business Card

Refer to existing design from attachments

Requirements
Must have
• Refer to existing design from attachments
Nice to have

```html
<!DOCTYPE html>
<html lang="en">
<head>
<meta charset="utf-8">
<title>Lenz Power Services – Business Card</title>
<link rel="stylesheet" href="https://fonts.googleapis.com/css2?family=Montserrat:wght@500;700&family=Open+Sans:wght@400;600;700&display=swap">
<style>
  :root {
    --page-bg: #ecebe8;
    --silver-light: #eef0f3;
    --silver-mid: #d3d7dc;
    --silver-dark: #b4bac2;
    --electric-blue: #1877e6;
    --blue-deep: #0b4aa8;
    --navy-band: #062457;
    --ink: #0f1b2d;
    --white: #ffffff;
  }
  * { box-sizing: border-box; margin: 0; padding: 0; }
  html, body { width: 1200px; height: 900px; overflow: hidden; }
  body {
    background: var(--page-bg);
    position: relative;
    font-family: "Open Sans", Arial, sans-serif;
    color: var(--ink);
  }
  .card {
    position: absolute;
    box-shadow: 0 6px 18px rgba(0,0,0,0.18);
    overflow: hidden;
  }
  .card-front {
    left: 238px; top: 62px; width: 555px; height: 341px;
    background: linear-gradient(135deg, var(--silver-light) 0%, var(--silver-mid) 55%, var(--silver-dark) 100%);
    color: var(--ink);
  }
  .card-back {
    left: 457px; top: 518px; width: 560px; height: 342px;
    background: linear-gradient(135deg, var(--electric-blue) 0%, var(--blue-deep) 100%);
    color: var(--white);
  }

  .holder-name {
    position: absolute; top: 24px; left: 0; width: 100%;
    text-align: center;
    font-family: "Montserrat", Arial, sans-serif; font-weight: 500;
    font-size: 22px; letter-spacing: 2px; text-transform: uppercase;
  }
  .holder-role {
    position: absolute; top: 52px; left: 0; width: 100%;
    text-align: center;
    font-family: "Montserrat", Arial, sans-serif; font-weight: 500;
    font-size: 15px; letter-spacing: 1.5px; text-transform: uppercase;
  }

  .brand {
    position: absolute;
    font-family: "Montserrat", Arial, sans-serif; font-weight: 700;
    text-transform: uppercase; line-height: 1;
  }
  .brand-main { display: block; }
  .brand-sub  { display: block; }

  .brand-mark {
    position: absolute; left: 100px; top: 116px;
    width: 80px; height: 80px; border-radius: 50%;
    background: var(--electric-blue);
  }
  .card-front .brand { left: 190px; top: 120px; color: var(--ink); }
  .card-front .brand-main { font-size: 62px; letter-spacing: 20px; }
  .card-front .brand-sub  { font-size: 21px; letter-spacing: 4.6px; margin-top: 6px; }

  .phone {
    position: absolute; top: 226px; left: 0; width: 100%;
    display: flex; justify-content: center; align-items: center; gap: 6px;
    font-size: 24px; font-weight: 400;
  }
  .phone svg { width: 16px; height: 20px; }
  .licence {
    position: absolute; top: 284px; left: 0; width: 100%;
    text-align: center;
    font-size: 13px; font-weight: 700;
  }

  .card-back .brand { left: 153px; top: 44px; color: var(--white); }
  .card-back .brand-main { font-size: 70px; letter-spacing: 24px; }
  .card-back .brand-sub  { font-size: 24px; letter-spacing: 5px; margin-top: 6px; }

  .tagline {
    position: absolute; top: 168px; left: 0; width: 100%;
    text-align: center;
    font-size: 20px; font-weight: 600; line-height: 28px;
    text-transform: uppercase; letter-spacing: 0.5px;
  }
  .contact-band {
    position: absolute; left: 0; top: 255px; width: 100%; height: 72px;
    background: var(--navy-band); color: var(--white);
    text-align: center;
  }
  .contact-band .cta {
    margin-top: 10px; font-size: 17px; font-weight: 600; letter-spacing: 0.3px;
    text-transform: uppercase;
  }
  .contact-band .details {
    margin-top: 6px; display: flex; justify-content: center; align-items: center;
    gap: 8px; font-size: 16px;
  }
  .contact-band .details span { display: inline-flex; align-items: center; gap: 6px; }
  .contact-band .details span + span { margin-left: 10px; }
  .contact-band svg { width: 13px; height: 13px; }
</style>
</head>
<body>

  <section class="card card-front" aria-label="Business card front">
    <p class="holder-name">Dario Lenz</p>
    <p class="holder-role">Director</p>

    <div class="brand-mark" aria-hidden="true"></div>
    <p class="brand">
      <span class="brand-main">Lenz</span>
      <span class="brand-sub">Power Services</span>
    </p>

    <p class="phone">
      <svg viewBox="0 0 16 20" aria-hidden="true"><path d="M4 1 L6.5 1 L7.5 5.5 L5.5 7 C6.3 10 7.5 12.5 9.5 14 L11.2 12.4 L15 14.5 L14.2 17.6 C13.5 18.8 12 19.2 10.5 18.6 C5.5 16.2 2 11 1.2 5.2 C1 3.2 2.2 1.5 4 1 Z" fill="#0f1b2d"/></svg>
      0400 123 456
    </p>
    <p class="licence">EC20394</p>
  </section>

  <section class="card card-back" aria-label="Business card back">
    <p class="brand">
      <span class="brand-main">Lenz</span>
      <span class="brand-sub">Power Services</span>
    </p>

    <p class="tagline">Your trusted<br>electrical contractor</p>

    <div class="contact-band">
      <p class="cta">Get in touch today for your free quotation</p>
      <p class="details">
        <span>
          <svg viewBox="0 0 13 13" aria-hidden="true"><rect x="0.5" y="2.5" width="12" height="8" fill="#fff"/><path d="M0.5 2.5 L6.5 7 L12.5 2.5" fill="none" stroke="#062457" stroke-width="1.2"/></svg>
          dario@lenzpower.com
        </span>
        <span>
          <svg viewBox="0 0 13 13" aria-hidden="true"><circle cx="6.5" cy="6.5" r="6" fill="#fff"/><path d="M3 4 C5 5 5 7 4 9 M8 2 C7 4 9 5 10.5 5 M9 9 C8 10 8.5 11 9.5 11.5" stroke="#062457" stroke-width="1.3" fill="none"/></svg>
          www.lenzpower.com.au
        </span>
      </p>
    </div>
  </section>

</body>
</html>
```